Verantis Guest Event Collateral

Create a double-sided, oversized piece of collateral for a series of guest networking events that we'll be hosting in 2019

We are looking for this piece of collateral to be the size of an oversized post card (1/2 of an 8/5 x 11 piece of paper). The front should include the following: Verantis's Mission Statement: Continually foster a culture of community and education for focused business professionals. How do we do it? Using four distinct principles, Verantis offers business professionals the opportunity to be successful right now ,as well as next year. Through in-person meetings, virtual meetings, networking events, and educational opportunities Verantis offers members a chance to hit their goals not only this year, but every year! Collaboration: Work with like-minded, driven Verantis members to collaborate and overcome the objections, hurdles and challenges that all business professionals face, either in person at twice monthly meetings, or virtually, from the comfort of your home or office. Accountability: Stay on track, and complete the goals you have set for yourself! Weekly in person or virtual meetings afford all members the opportunity to review their plan twice a month with fellow Verantis members, and trained Verantis coaches. Referrals: In the midst of crafting an executable, measurable and attainable plan let Verantis build your business through a steady stream of referrals via six yearly networking events, specifically designed to ensure you walk away with new referral partners. Strategy: Let Verantis assist you in crafting a strategy within our proven business planning template; realistic, understandable, measurable, beyond normal, attainable and time bound. The back should include the following: Become a Verantis member for $150/month and join us for 6 Networking Events in 2019 plus much more! We aren’t just about collaboration, accountability and strategy! Creating opportunities for referrals is also a cornerstone of Verantis! To make certain we are delivering on this principle, Verantis will host 6 events throughout 2019, complete with specific activities at each event to ensure you meet everyone in the room, making immediate connects to build your referral network. Join now and put yourself in position for success in 2019! Name: Phone: Email: Company Name: Industry: Position: Credit Card Number: Exp. Date: Testimonials: Overall I think people are lazy. I know I am! The benefits I have found and have come to truly appreciate thru Verantis are a sense of professionalism, accountability and shared enthusiasm. These things break that cycle of laziness for me and, I am sure, many others. When I walk into a meeting I know that positive and helpful feedback is the name of the game. Feedback from others and in many other industries from my own has become a key and cornerstone to my business and personal success. I would urge anyone no matter what your occupation to attend a couple of meetings and see how this group of like minded professionals can help you to achieve more. More time, More success, More health, More security, More money, More happiness..............What could you use more of? Gordon T. Melby Sr. Automotive Consultant Ridgewater Leasing & Sales Thank you!

Target Market(s)

Small business owners, entrpreneurs, networkers, sales people

Industry/Entity Type

Business Consultant

Font styles to use
Sans Serif

Colors
f36f22
f68d4e
f8ba93
f78f20
faa54b

Requirements
Must have
• - Imagery
• - Our company logo
• - Clear CTA to check out our website (www.verantis-example.com)
• - Option to "Join the Verantis Community Today!" and include a spot for someone to fill in their name, email address, company name, and phone number
• - Reference that we host 6+ networking events in Denver throughout the year that are free to attend and are unlike any other networking event they've attended before
• - Mention that we have in-person meetings 2x per month, virtual meeting options, networking events, and educational events
• - Highlight the following acronym which references our core company components:
• Collaboration:
• Work with like-minded, driven Verantis members to collaborate and overcome the objections, hurdles and challenges that all business professionals face, in either in person twice monthly meetings, or virtually, from the comfort of your home of office.
• Accountability:
• Stay on track, and complete the goals you have set for yourself! Weekly in person or virtual meetings afford all members the opportunity to review their plan twice a month with your fellow Verantis members and trained Verantis coaches, to make certain you success is continuous throughout the year.
• Referrals:
• In the midst of crafting an executable, measurable and attainable plan let Verantis build your business through a steady stream of referral opportunities via twelve yearly networking events, specifically designed to ensure you walk away with new referral partners.
• Strategy:
• Let Verantis assist you in crafting a strategy within our proven business planning template; realistic, understandable, measurable, beyond normal, attainable and time bound.

```html
<!DOCTYPE html>
<html lang="en">
<head>
<meta charset="utf-8">
<title>Verantis Guest Networking Events 2019</title>
<link href="https://fonts.googleapis.com/css2?family=Montserrat:wght@400;500;600&family=Lato:wght@400;700&display=swap" rel="stylesheet">
<style>
  :root {
    --orange: #f36f22;
    --orange-mid: #f78f20;
    --orange-soft: #f68d4e;
    --orange-pale: #f8ba93;
    --ink: #2f3440;
    --ink-soft: #3b3f47;
    --header-grey: #e4e4e4;
    --paper: #ffffff;
    --paper-tint: #f4f5f7;
    --backdrop: #ececec;
    --rule: #6b6f76;
  }
  * { margin: 0; padding: 0; box-sizing: border-box; }
  html, body { width: 1200px; height: 800px; overflow: hidden; }
  body {
    background: var(--backdrop);
    font-family: "Lato", sans-serif;
    position: relative;
  }
  .sheet {
    position: absolute;
    top: 83px;
    width: 490px;
    height: 634px;
    background: linear-gradient(180deg, var(--paper) 0%, var(--paper-tint) 100%);
    overflow: hidden;
  }
  .sheet--front { left: 70px; }
  .sheet--back { left: 640px; }

  .hero-photo {
    position: absolute; left: 0; top: 0; width: 490px; height: 276px;
    background: linear-gradient(115deg, #b9b3ad 0%, #9a8f86 30%, #6d6a6c 55%, #4b4f58 80%, #3d424b 100%);
  }
  .hero-shapes { position: absolute; left: 0; top: 0; width: 490px; height: 320px; }
  .footer-shapes { position: absolute; left: 0; top: 596px; width: 490px; height: 38px; }

  .brand {
    position: absolute; left: 24px; top: 33px;
    display: flex; align-items: center; gap: 6px;
    font-family: "Montserrat", sans-serif; font-weight: 400;
    font-size: 21px; letter-spacing: 0.5px; color: var(--ink-soft);
  }
  .brand__mark { width: 20px; height: 20px; background: var(--orange); }

  .headline { position: absolute; left: 24px; top: 133px; color: var(--ink); font-family: "Montserrat", sans-serif; }
  .headline__kicker { font-size: 17px; font-weight: 400; letter-spacing: 0.3px; line-height: 1; }
  .headline__main { font-size: 33px; font-weight: 500; letter-spacing: 0.8px; line-height: 1.05; }

  .banner-text {
    position: absolute; left: 14px; top: 266px;
    font-family: "Montserrat", sans-serif; font-weight: 500;
    font-size: 14px; letter-spacing: 0.6px; color: #fff;
  }
  .sheet--back .banner-text { left: 24px; top: 262px; font-size: 17px; color: var(--ink); }

  .cta-pill {
    position: absolute; left: 100px; top: 325px; width: 308px; height: 40px;
    background: var(--ink); border-radius: 20px;
    color: #fff; font-family: "Montserrat", sans-serif; font-weight: 500;
    font-size: 15px; letter-spacing: 0.8px;
    display: flex; align-items: center; justify-content: center;
  }
  .signup-form {
    position: absolute; left: 43px; top: 390px; width: 393px; height: 168px;
    border: 1px solid var(--rule); border-radius: 16px; background: rgba(255,255,255,0.6);
  }
  .signup-form__row {
    position: absolute; left: 13px; right: 18px;
    display: flex; align-items: flex-end;
  }
  .signup-form__label {
    width: 95px; font-family: "Montserrat", sans-serif; font-size: 8.5px;
    color: var(--orange); letter-spacing: 0.3px;
  }
  .signup-form__line { flex: 1; border-bottom: 1px solid var(--rule); height: 1px; margin-bottom: 2px; }

  .footer-url {
    position: absolute; left: 44px; top: 604px;
    font-family: "Lato", sans-serif; font-weight: 700; font-size: 13px; color: #fff;
  }
  .footer-social {
    position: absolute; top: 618px; display: flex; align-items: center; gap: 5px;
    font-size: 8px; color: #fff;
  }
  .footer-social__dot { width: 6px; height: 6px; background: #4aa3df; }

  .components-divider { position: absolute; left: 235px; top: 312px; width: 2px; height: 252px; background: var(--ink-soft); }
  .component { position: absolute; width: 170px; }
  .component__tag { position: relative; height: 22px; display: flex; align-items: center; }
  .component__icon {
    position: relative; z-index: 1;
    width: 24px; height: 24px; border-radius: 50%; background: #fff;
    border: 2px solid var(--orange); display: flex; align-items: center; justify-content: center;
  }
  .component__name {
    margin-left: -10px; height: 18px; padding-left: 16px; width: 134px;
    background: var(--orange); border-radius: 0 9px 9px 0;
    color: #fff; font-family: "Montserrat", sans-serif; font-weight: 600;
    font-size: 10px; letter-spacing: 0.4px; display: flex; align-items: center;
  }
  .component--large .component__name { font-size: 13px; width: 130px; padding-left: 22px; }
  .component__copy { margin-top: 16px; font-size: 8.2px; line-height: 1.28; color: var(--ink); }
  .component--large .component__copy { font-size: 8px; margin-top: 14px; }
</style>
</head>
<body>

<!-- FRONT: sign-up side -->
<section class="sheet sheet--front">
  <div class="hero-photo" role="img" aria-label="Photo of business professionals reviewing printed charts and reports at a desk"></div>
  <svg class="hero-shapes" viewBox="0 0 490 320" aria-hidden="true">
    <polygon points="0,0 228,0 174,84 0,84" fill="var(--header-grey)"/>
    <polygon points="228,0 238,0 184,86 174,86" fill="var(--orange-mid)"/>
    <rect x="0" y="84" width="182" height="3" fill="var(--orange-mid)"/>
    <polygon points="0,255 365,255 380,295 0,295" fill="var(--orange-mid)"/>
    <polygon points="330,295 380,295 313,312" fill="var(--orange-soft)"/>
  </svg>
  <div class="brand"><span class="brand__mark"></span>VERANTIS</div>
  <div class="headline">
    <div class="headline__kicker">GUEST NETWORKING</div>
    <div class="headline__main">EVENTS IN 2019</div>
  </div>
  <div class="banner-text">"JOIN THE VERANTIS COMMUNITY TODAY!"</div>

  <div class="cta-pill">WANT TO FIND OUT MORE?</div>
  <div class="signup-form">
    <div class="signup-form__row" style="top:40px"><span class="signup-form__label">NAME -</span><span class="signup-form__line"></span></div>
    <div class="signup-form__row" style="top:63px"><span class="signup-form__label">EMAIL-ADRESS -</span><span class="signup-form__line"></span></div>
    <div class="signup-form__row" style="top:87px"><span class="signup-form__label">COMPANY NAME -</span><span class="signup-form__line"></span></div>
    <div class="signup-form__row" style="top:110px"><span class="signup-form__label">CONTACT NUMBER-</span><span class="signup-form__line"></span></div>
  </div>

  <svg class="footer-shapes" viewBox="0 0 490 38" aria-hidden="true">
    <rect x="0" y="14" width="490" height="24" fill="var(--ink)"/>
    <polygon points="0,6 232,6 220,28 0,28" fill="var(--orange-soft)"/>
  </svg>
  <div class="footer-url">www.verantis-example.com</div>
  <div class="footer-social" style="left:242px"><span class="footer-social__dot"></span>social.verantis-example.com</div>
  <div class="footer-social" style="left:380px"><span class="footer-social__dot"></span>news.verantis-example.com</div>
</section>

<!-- BACK: core components side -->
<section class="sheet sheet--back">
  <div class="hero-photo" role="img" aria-label="Photo of business professionals reviewing printed charts and reports at a desk"></div>
  <svg class="hero-shapes" viewBox="0 0 490 320" aria-hidden="true">
    <polygon points="0,0 228,0 174,84 0,84" fill="var(--header-grey)"/>
    <polygon points="228,0 238,0 184,86 174,86" fill="var(--orange-mid)"/>
    <rect x="0" y="84" width="182" height="3" fill="var(--orange-mid)"/>
    <polygon points="0,255 360,255 380,293 0,293" fill="var(--orange-mid)"/>
    <polygon points="322,293 375,293 313,310" fill="var(--orange-soft)"/>
  </svg>
  <div class="brand"><span class="brand__mark"></span>VERANTIS</div>
  <div class="headline">
    <div class="headline__kicker">GUEST NETWORKING</div>
    <div class="headline__main">EVENTS IN 2019</div>
  </div>
  <div class="banner-text">CORE COMPANY COMPONENTS:</div>

  <div class="components-divider"></div>

  <article class="component" style="left:34px; top:330px">
    <div class="component__tag">
      <span class="component__icon"><svg width="14" height="12" viewBox="0 0 14 12"><circle cx="5" cy="3" r="2.5" fill="var(--orange)"/><path d="M0 12 Q5 5 10 12Z" fill="var(--orange)"/><circle cx="11" cy="4" r="1.8" fill="var(--orange-pale)"/></svg></span>
      <span class="component__name">COLLABORATION</span>
    </div>
    <p class="component__copy">Work with like-minded, driven Verantis members to collaborate and overcome the objections, hurdles and challenges that all business professionals face, in either in person twice monthly meetings, or virtually, from the comfort of your home or office.</p>
  </article>

  <article class="component" style="left:34px; top:457px">
    <div class="component__tag">
      <span class="component__icon"><svg width="10" height="12" viewBox="0 0 10 12"><rect x="0.5" y="0.5" width="9" height="11" fill="none" stroke="var(--orange)"/><path d="M2 4H8M2 6.5H8M2 9H6" stroke="var(--orange)"/></svg></span>
      <span class="component__name">ACCOUNTABILITY</span>
    </div>
    <p class="component__copy">Stay on track, and complete the goals you have set for yourself! Weekly in person or virtual meetings afford all members the opportunity to review their plan twice a month with your fellow Verantis members and trained Verantis coaches.</p>
  </article>

  <article class="component component--large" style="left:267px; top:331px">
    <div class="component__tag">
      <span class="component__icon"><svg width="12" height="10" viewBox="0 0 12 10"><rect x="1" y="6" width="2" height="4" fill="var(--orange)"/><rect x="4" y="4" width="2" height="6" fill="var(--orange)"/><rect x="7" y="2" width="2" height="8" fill="var(--orange)"/><rect x="10" y="0" width="2" height="10" fill="var(--orange)"/></svg></span>
      <span class="component__name">REFERRALS</span>
    </div>
    <p class="component__copy">In the midst of crafting an executable, measurable and attainable plan let Verantis build your business through a steady stream of referral opportunities via twelve yearly networking events, specifically designed to ensure you walk away with new referral partners.</p>
  </article>

  <article class="component component--large" style="left:267px; top:458px">
    <div class="component__tag">
      <span class="component__icon"><svg width="14" height="10" viewBox="0 0 14 10"><polygon points="7,0 14,3.5 7,7 0,3.5" fill="var(--orange)"/><path d="M3 5V8Q7 10 11 8V5" fill="var(--orange)"/></svg></span>
      <span class="component__name">STRATEGY</span>
    </div>
    <p class="component__copy">Let Verantis assist you in crafting a strategy within our proven business planning template; realistic, understandable, measurable, beyond normal, attainable and time bound.</p>
  </article>

  <svg class="footer-shapes" viewBox="0 0 490 38" aria-hidden="true">
    <rect x="0" y="14" width="490" height="24" fill="var(--ink)"/>
    <polygon points="0,6 232,6 220,28 0,28" fill="var(--orange-soft)"/>
  </svg>
  <div class="footer-url">www.verantis-example.com</div>
  <div class="footer-social" style="left:242px"><span class="footer-social__dot"></span>social.verantis-example.com</div>
  <div class="footer-social" style="left:380px"><span class="footer-social__dot"></span>news.verantis-example.com</div>
</section>

</body>
</html>
```